Loops & Ledgers - Promo Card

This is my first go at this... but I need some Business Card sized promotional material that we can hand out to customers at our retail store.
The promotional cards are designed to drive traffic for specific areas of our business, at specific times. We often staple them to customer receipts, but also will be handing them out to employees of major retailers as preferred customer cards for specific periods of time.
======================================================
Video Games:
(Standard) Loops & Ledgers VIP Customer Card
(Editable Text) On _________ receive 10% off all video game purchases
I want the "Editable Text" to allow us to easily change the criteria of the promo, or the date of the promo. Basically I am looking for a template that I can quickly send to the printshop when we have an idea.
I have some graphics with out logo, and past billboard we have used which could be used to see logo/colour (Do not use dog from billboard image). If we like the work there is a relatively significant amount of additional design work for signage, display cards, and the like around the store.
I have a .PSD file of our billboard... but it is 39MB and the software will not allow me to upload anything beyond 30MB. So I have attached a low res JPG. It should give you an idea of who we are though, the designer was from Winnipeg and well... you'll see.
For reference our website is: www.loopsledgers.example
Target Market(s)
18-45 (male/female), low->midupper income, highschool->university education
Industry/Entity Type
Software
Look and feel

```html
<!DOCTYPE html>
<html lang="en">
<head>
<meta charset="utf-8">
<title>Loops &amp; Ledgers – Promo Card</title>
<link rel="stylesheet" href="https://fonts.googleapis.com/css2?family=Roboto+Condensed:wght@700&family=Arimo:wght@700&display=swap">
<style>
  :root {
    --backdrop: #1f1f1f;
    --yellow: #f8e321;
    --yellow-warm: #f1d91c;
    --slate: #3e4f58;
    --white: #ffffff;
    --panel: #ececec;
  }
  * { margin: 0; padding: 0; box-sizing: border-box; }
  html, body { width: 1200px; height: 900px; overflow: hidden; }
  body {
    background: radial-gradient(ellipse at 40% 35%, #3a3a3a 0%, var(--backdrop) 70%, #111 100%);
    position: relative;
    font-family: "Arimo", Arial, sans-serif;
  }

  /* ---------- Front of card ---------- */
  .card-front {
    position: absolute;
    width: 315px; height: 180px;
    background: var(--yellow);
    overflow: hidden;
  }
  .card-front.is-textured { background: var(--yellow-warm); }
  .card-front .band-top,
  .card-front .band-bottom {
    position: absolute; left: 0; width: 100%;
    background: var(--slate);
  }
  .card-front .band-top { top: 0; height: 10px; border-bottom: 3px solid var(--white); box-sizing: content-box; }
  .card-front .band-bottom { bottom: 0; height: 11px; border-top: 3px solid var(--white); box-sizing: content-box; }
  .card-front .stripes-top { position: absolute; left: 4px; top: 0; }
  .card-front .stripes-bottom { position: absolute; right: 4px; bottom: 0; }
  .brand-lockup {
    position: absolute; left: 0; right: 0; top: 58px;
    text-align: center; color: var(--slate);
  }
  .brand-name {
    display: flex; align-items: center; justify-content: center; gap: 8px;
    font-size: 29px; line-height: 1; letter-spacing: -0.3px;
  }
  .brand-name .brand-dot {
    width: 12px; height: 12px; border-radius: 50%; background: var(--slate);
  }
  .tagline {
    margin-top: 10px;
    font-size: 15px; letter-spacing: 0.3px;
  }

  /* ---------- Back of card ---------- */
  .card-back {
    position: absolute;
    width: 180px; height: 315px;
    background: var(--yellow);
    overflow: hidden;
    font-family: "Arimo", Arial, sans-serif;
  }
  .card-back.is-textured { background: var(--yellow-warm); }
  .promo-category {
    position: absolute; top: 20px; left: 0; right: 0;
    text-align: center;
    font-family: "Roboto Condensed", "Arial Narrow", sans-serif;
    font-size: 21px; color: var(--slate); letter-spacing: 0.2px;
  }
  .promo-date-field {
    position: absolute; top: 60px; left: 28px;
    width: 122px; height: 44px;
    background: var(--panel); border-radius: 3px;
    display: flex; align-items: center; padding-left: 17px;
    font-size: 12px; color: var(--slate);
  }
  .promo-date-field .blank {
    display: inline-block; width: 60px; margin-left: 6px;
    border-bottom: 1.5px solid var(--slate); transform: translateY(3px);
  }
  .offer {
    position: absolute; left: 20px; top: 118px;
    width: 140px; height: 122px;
    background: var(--slate); border-radius: 16px;
    text-align: center; color: var(--white);
    padding-top: 4px;
  }
  .offer-verb { font-size: 30px; line-height: 32px; letter-spacing: -0.5px; }
  .offer-amount { font-size: 56px; line-height: 48px; color: var(--yellow); letter-spacing: -2px; }
  .offer-scope { font-size: 10.5px; line-height: 14px; margin-top: 3px; }
  .offer-object { font-size: 19px; line-height: 20px; }
  .card-back .footer-band {
    position: absolute; left: 0; bottom: 0; width: 100%; height: 40px;
    background: var(--slate); border-top: 3px solid var(--white);
    box-sizing: content-box;
    display: flex; align-items: center; justify-content: center;
    padding-top: 4px;
    font-size: 13.5px; color: var(--yellow);
  }
  .card-back .stripes-footer { position: absolute; left: 0; top: 0; }
</style>
</head>
<body>

  <!-- Set 1 -->
  <section class="card-front is-textured" style="left:344px; top:253px;">
    <div class="band-top">
      <svg class="stripes-top" width="44" height="10" viewBox="0 0 44 10"><g stroke="#f8e321" stroke-width="1.6"><line x1="0" y1="10" x2="10" y2="0"/><line x1="7" y1="10" x2="17" y2="0"/><line x1="14" y1="10" x2="24" y2="0"/><line x1="21" y1="10" x2="31" y2="0"/></g></svg>
    </div>
    <div class="brand-lockup">
      <div class="brand-name"><span class="brand-dot"></span>Loops &amp; Ledgers</div>
      <div class="tagline">The Deals are Here!</div>
    </div>
    <div class="band-bottom">
      <svg class="stripes-bottom" width="44" height="11" viewBox="0 0 44 11"><g stroke="#f8e321" stroke-width="1.6"><line x1="0" y1="11" x2="11" y2="0"/><line x1="7" y1="11" x2="18" y2="0"/><line x1="14" y1="11" x2="25" y2="0"/><line x1="21" y1="11" x2="32" y2="0"/></g></svg>
    </div>
  </section>

  <section class="card-back is-textured" style="left:676px; top:118px;">
    <h2 class="promo-category">VIDEO GAMES</h2>
    <div class="promo-date-field">ON<span class="blank"></span></div>
    <div class="offer">
      <div class="offer-verb">receive</div>
      <div class="offer-amount">10%</div>
      <div class="offer-scope">OFF ALL VIDEO GAME</div>
      <div class="offer-object">PURCHASES</div>
    </div>
    <div class="footer-band">
      <svg class="stripes-footer" width="60" height="40" viewBox="0 0 60 40"><g stroke="#f8e321" stroke-width="1.6"><line x1="0" y1="22" x2="22" y2="0"/><line x1="0" y1="30" x2="30" y2="0"/><line x1="0" y1="38" x2="38" y2="0"/></g></svg>
      www.loopsledgers.example
    </div>
  </section>

  <!-- Set 2 -->
  <section class="card-front" style="left:344px; top:603px;">
    <div class="band-top">
      <svg class="stripes-top" width="44" height="10" viewBox="0 0 44 10"><g stroke="#f8e321" stroke-width="1.6"><line x1="0" y1="10" x2="10" y2="0"/><line x1="7" y1="10" x2="17" y2="0"/><line x1="14" y1="10" x2="24" y2="0"/><line x1="21" y1="10" x2="31" y2="0"/></g></svg>
    </div>
    <div class="brand-lockup">
      <div class="brand-name"><span class="brand-dot"></span>Loops &amp; Ledgers</div>
      <div class="tagline">The Deals are Here!</div>
    </div>
    <div class="band-bottom">
      <svg class="stripes-bottom" width="44" height="11" viewBox="0 0 44 11"><g stroke="#f8e321" stroke-width="1.6"><line x1="0" y1="11" x2="11" y2="0"/><line x1="7" y1="11" x2="18" y2="0"/><line x1="14" y1="11" x2="25" y2="0"/><line x1="21" y1="11" x2="32" y2="0"/></g></svg>
    </div>
  </section>

  <section class="card-back" style="left:676px; top:468px;">
    <h2 class="promo-category">VIDEO GAMES</h2>
    <div class="promo-date-field">ON<span class="blank"></span></div>
    <div class="offer">
      <div class="offer-verb">receive</div>
      <div class="offer-amount">10%</div>
      <div class="offer-scope">OFF ALL VIDEO GAME</div>
      <div class="offer-object">PURCHASES</div>
    </div>
    <div class="footer-band">
      <svg class="stripes-footer" width="60" height="40" viewBox="0 0 60 40"><g stroke="#f8e321" stroke-width="1.6"><line x1="0" y1="22" x2="22" y2="0"/><line x1="0" y1="30" x2="30" y2="0"/><line x1="0" y1="38" x2="38" y2="0"/></g></svg>
      www.loopsledgers.example
    </div>
  </section>

</body>
</html>
```